creating professional text layers for Varnello Product listings images

I need some text added to several images in a professional eye catching way. The text should be legible on desktop and mobile devices. Rough mocks will be provided. You will just need to make them pop and professional. There are 10 images required in total to the selected designer. Below are just 3 of them

```html
<!DOCTYPE html>
<html lang="en">
<head>
<meta charset="UTF-8">
<title>Variable Speed Control – Listing Image</title>
<link rel="stylesheet" href="https://fonts.googleapis.com/css2?family=Montserrat:wght@600;700;800&display=swap">
<style>
  :root {
    --bg-dark: #0b0b0b;
    --bg-mid: #2a2a2a;
    --machine-gray: #8a8d90;
    --machine-cream: #e6dfcc;
    --callout-red: #e41f26;
    --callout-shadow: #9e1016;
    --headline-cream: #ece3cc;
    --white: #ffffff;
  }
  html, body {
    margin: 0;
    padding: 0;
    width: 1200px;
    height: 1200px;
    overflow: hidden;
    background: var(--bg-dark);
  }
  .canvas {
    position: relative;
    width: 1200px;
    height: 1200px;
    overflow: hidden;
    font-family: "Montserrat", sans-serif;
  }
  .product-photo {
    position: absolute;
    inset: 0;
    background:
      radial-gradient(ellipse 320px 560px at 290px 560px, var(--machine-cream) 0%, var(--machine-gray) 45%, rgba(40,40,40,0) 100%),
      radial-gradient(ellipse 360px 520px at 880px 900px, #5a5a5a 0%, rgba(30,30,30,0) 100%),
      linear-gradient(180deg, var(--bg-dark) 0%, var(--bg-mid) 70%, #3a3a3a 100%);
  }
  .callout {
    position: absolute;
    inset: 0;
    width: 1200px;
    height: 1200px;
  }
  .callout-shape { fill: var(--callout-red); }
  .headline {
    position: absolute;
    left: 608px;
    top: 470px;
    margin: 0;
    font-weight: 600;
    font-size: 96px;
    line-height: 88px;
    letter-spacing: -1px;
    color: var(--headline-cream);
    text-transform: uppercase;
    text-shadow:
      1px 2px 0 var(--callout-shadow),
      2px 4px 0 var(--callout-shadow),
      3px 6px 0 var(--callout-shadow),
      4px 8px 0 var(--callout-shadow),
      5px 10px 6px rgba(90, 6, 10, 0.6);
  }
  .subline {
    position: absolute;
    left: 622px;
    top: 852px;
    margin: 0;
    font-weight: 700;
    font-size: 38px;
    line-height: 43px;
    color: var(--white);
    text-transform: uppercase;
  }
</style>
</head>
<body>
  <main class="canvas">
    <div class="product-photo" role="img" aria-label="Photo of the wire stripping machine: grey motor with cream control box, speed dial, emergency stop button and red power switch, with the hand wheel and stripping blades on the right, on a black background"></div>

    <svg class="callout" viewBox="0 0 1200 1200" aria-hidden="true">
      <path class="callout-shape" d="M525 442 Q525 409 558 409 L1188 409 Q1200 409 1200 421 L1200 918 C1150 872 1100 818 1035 818 L550 818 Q525 818 525 793 Z"/>
    </svg>

    <h1 class="headline">Variable<br>Speed<br>Control</h1>
    <p class="subline">How could<br>you possibly<br>strip all gauges<br>at the same<br>speed?</p>
  </main>
</body>
</html>
```